" A nossa empresa trabalha com um vale-refeição digital. Fechamos contratos com restaurantes para que eles possam receber a nossa forma de pagamento (cartãozinho do Grupo da Mesada e QR CODE do celular do usuário). Fechamos, então, contratos com empresas para que elas usem o nosso vale-refeição digital, com os usuários delas podendo pesquisar por prato (cardápio), estilo de comida (a la carte, buffet), estilo de cozinha (italiana, alemã, etc) na região onde trabalham (geolocalização) "

```html
<!DOCTYPE html>
<html lang="pt-BR">
<head>
<meta charset="UTF-8">
<title>Grupo da Mesada — Novos clientes para o seu restaurante</title>
<link href="https://fonts.googleapis.com/css2?family=Montserrat:wght@400;500;700;800&display=swap" rel="stylesheet">
<style>
  :root{
    --red:#b5243b;
    --red-dark:#961a2f;
    --ink:#4a4a4a;
    --muted:#9a9a9a;
    --line:#e6e6e6;
    --page:#eeeeee;
    --screen:#ffffff;
    --teal:#2fa39a;
    --orange:#f0a23a;
    --purple:#6b5ca5;
    --pink:#d9577a;
    --yellow:#f3cf4a;
    --green:#8cbf4f;
  }
  *{box-sizing:border-box;margin:0;padding:0}
  html,body{width:1200px;height:1200px;overflow:hidden}
  body{background:var(--page);font-family:"Montserrat",Arial,sans-serif;color:var(--ink);position:relative}

  .screen{position:absolute;left:40px;top:180px;width:1120px;height:840px;background:var(--screen);display:flex;box-shadow:0 2px 10px rgba(0,0,0,.08)}

  /* dashboard */
  .sidebar{width:90px;background:var(--red);color:#fff;padding:18px 10px;font-size:9px}
  .sidebar .brand{display:flex;align-items:center;gap:5px;font-weight:700;font-size:9px;margin-bottom:26px}
  .sidebar .brand i{width:10px;height:10px;border-radius:50%;background:#fff;flex:none}
  .sidebar ul{list-style:none}
  .sidebar li{padding:7px 0;border-bottom:1px solid rgba(255,255,255,.18);opacity:.9}

  .dashboard{width:470px;padding:14px 22px;border-right:1px solid var(--line)}
  .topbar{font-size:9px;color:var(--muted);text-align:center;margin-bottom:16px}
  .dash-title{font-size:17px;font-weight:700;color:var(--red);padding-left:20px}
  .dash-sub{font-size:8px;color:var(--muted);padding-left:20px;margin:3px 0 12px}
  .tabs{display:flex;gap:14px;padding-left:20px;margin-bottom:18px}
  .tabs span{width:120px;height:34px;display:flex;align-items:center;justify-content:center;font-size:8px;font-weight:700;color:#fff;background:#c9c9c9}
  .tabs span.active{background:var(--red)}
  .charts{display:grid;grid-template-columns:repeat(3,128px);gap:14px 12px;padding-left:14px}
  .card{height:132px;border:1px solid var(--line);background:#fff;display:flex;flex-direction:column;align-items:center}
  .card h4{width:100%;font-size:7px;font-weight:500;text-align:center;color:#fff;background:var(--red);padding:4px 0}
  .card svg{width:84px;height:84px;margin-top:14px}

  /* pitch */
  .pitch{flex:1;padding:40px 46px 0 40px;position:relative}
  .headline{text-align:right;font-size:27px;line-height:1.18;font-weight:500;color:var(--ink);text-transform:uppercase;letter-spacing:.3px}
  .headline b{color:var(--red);font-weight:800}
  .preview{margin:34px 0 0 40px;width:440px;height:250px;transform:perspective(900px) rotateY(-14deg) rotateX(6deg);background:linear-gradient(135deg,#f7f7f7 0%,#e9e9ee 60%,#d9d9e2 100%);border-left:26px solid var(--red);box-shadow:0 18px 30px rgba(0,0,0,.15)}
  .steps{list-style:none;margin-top:46px}
  .steps li{display:flex;align-items:flex-start;gap:14px;margin-bottom:22px;font-size:14px;line-height:1.3;text-transform:uppercase}
  .steps .num{font-size:42px;font-weight:800;color:var(--red);line-height:.9;width:28px;flex:none}
  .steps b{color:var(--red);font-weight:700}
</style>
</head>
<body>
<section class="screen">
  <nav class="sidebar">
    <div class="brand"><i></i>Grupo da Mesada</div>
    <ul>
      <li>Início</li><li>Pedidos</li><li>Cardápio</li><li>Relatórios</li><li>Usuários</li><li>Configurações</li>
    </ul>
  </nav>

  <div class="dashboard">
    <p class="topbar">Painel do restaurante</p>
    <h2 class="dash-title">Dados Importantes</h2>
    <p class="dash-sub">Resumo do mês atual</p>
    <div class="tabs"><span class="active">Pratos vendidos</span><span>Horários</span></div>

    <div class="charts">
      <div class="card"><h4>Estilo cozinha</h4>
        <svg viewBox="0 0 42 42"><circle cx="21" cy="21" r="15.915" fill="none" stroke="var(--teal)" stroke-width="8" stroke-dasharray="40 60" stroke-dashoffset="25"/><circle cx="21" cy="21" r="15.915" fill="none" stroke="var(--orange)" stroke-width="8" stroke-dasharray="30 70" stroke-dashoffset="-15"/><circle cx="21" cy="21" r="15.915" fill="none" stroke="var(--purple)" stroke-width="8" stroke-dasharray="30 70" stroke-dashoffset="-45"/></svg></div>
      <div class="card"><h4>Tipo prato</h4>
        <svg viewBox="0 0 42 42"><circle cx="21" cy="21" r="15.915" fill="none" stroke="var(--red)" stroke-width="8" stroke-dasharray="55 45" stroke-dashoffset="25"/><circle cx="21" cy="21" r="15.915" fill="none" stroke="var(--yellow)" stroke-width="8" stroke-dasharray="25 75" stroke-dashoffset="-30"/><circle cx="21" cy="21" r="15.915" fill="none" stroke="var(--teal)" stroke-width="8" stroke-dasharray="20 80" stroke-dashoffset="-55"/></svg></div>
      <div class="card"><h4>Dia semana</h4>
        <svg viewBox="0 0 42 42"><circle cx="21" cy="21" r="15.915" fill="none" stroke="var(--green)" stroke-width="8" stroke-dasharray="35 65" stroke-dashoffset="25"/><circle cx="21" cy="21" r="15.915" fill="none" stroke="var(--pink)" stroke-width="8" stroke-dasharray="35 65" stroke-dashoffset="-10"/><circle cx="21" cy="21" r="15.915" fill="none" stroke="var(--orange)" stroke-width="8" stroke-dasharray="30 70" stroke-dashoffset="-45"/></svg></div>
      <div class="card"><h4>Faixa horária</h4>
        <svg viewBox="0 0 42 42"><circle cx="21" cy="21" r="15.915" fill="none" stroke="var(--pink)" stroke-width="8" stroke-dasharray="60 40" stroke-dashoffset="25"/><circle cx="21" cy="21" r="15.915" fill="none" stroke="var(--purple)" stroke-width="8" stroke-dasharray="40 60" stroke-dashoffset="-35"/></svg></div>
      <div class="card"><h4>Forma pagamento</h4>
        <svg viewBox="0 0 42 42"><circle cx="21" cy="21" r="15.915" fill="none" stroke="var(--red)" stroke-width="8" stroke-dasharray="70 30" stroke-dashoffset="25"/><circle cx="21" cy="21" r="15.915" fill="none" stroke="var(--orange)" stroke-width="8" stroke-dasharray="30 70" stroke-dashoffset="-45"/></svg></div>
      <div class="card"><h4>Novos clientes</h4>
        <svg viewBox="0 0 42 42"><circle cx="21" cy="21" r="15.915" fill="none" stroke="var(--red)" stroke-width="8" stroke-dasharray="45 55" stroke-dashoffset="25"/><circle cx="21" cy="21" r="15.915" fill="none" stroke="var(--pink)" stroke-width="8" stroke-dasharray="35 65" stroke-dashoffset="-20"/><circle cx="21" cy="21" r="15.915" fill="none" stroke="var(--yellow)" stroke-width="8" stroke-dasharray="20 80" stroke-dashoffset="-55"/></svg></div>
      <div class="card"><h4>Região usuários</h4>
        <svg viewBox="0 0 42 42"><circle cx="21" cy="21" r="15.915" fill="none" stroke="var(--teal)" stroke-width="8" stroke-dasharray="50 50" stroke-dashoffset="25"/><circle cx="21" cy="21" r="15.915" fill="none" stroke="var(--green)" stroke-width="8" stroke-dasharray="25 75" stroke-dashoffset="-25"/><circle cx="21" cy="21" r="15.915" fill="none" stroke="var(--purple)" stroke-width="8" stroke-dasharray="25 75" stroke-dashoffset="-50"/></svg></div>
      <div class="card"><h4>Ticket médio</h4>
        <svg viewBox="0 0 42 42"><circle cx="21" cy="21" r="15.915" fill="none" stroke="var(--orange)" stroke-width="8" stroke-dasharray="65 35" stroke-dashoffset="25"/><circle cx="21" cy="21" r="15.915" fill="none" stroke="var(--teal)" stroke-width="8" stroke-dasharray="35 65" stroke-dashoffset="-40"/></svg></div>
      <div class="card"><h4>Avaliação geral</h4>
        <svg viewBox="0 0 42 42"><circle cx="21" cy="21" r="15.915" fill="none" stroke="var(--purple)" stroke-width="8" stroke-dasharray="55 45" stroke-dashoffset="25"/><circle cx="21" cy="21" r="15.915" fill="none" stroke="var(--yellow)" stroke-width="8" stroke-dasharray="45 55" stroke-dashoffset="-30"/></svg></div>
      <div class="card"><h4>Buffet livre</h4>
        <svg viewBox="0 0 42 42"><circle cx="21" cy="21" r="15.915" fill="none" stroke="var(--orange)" stroke-width="8" stroke-dasharray="40 60" stroke-dashoffset="25"/><circle cx="21" cy="21" r="15.915" fill="none" stroke="var(--teal)" stroke-width="8" stroke-dasharray="35 65" stroke-dashoffset="-15"/><circle cx="21" cy="21" r="15.915" fill="none" stroke="var(--red)" stroke-width="8" stroke-dasharray="25 75" stroke-dashoffset="-50"/></svg></div>
      <div class="card"><h4>Prato feito</h4>
        <svg viewBox="0 0 42 42"><circle cx="21" cy="21" r="15.915" fill="none" stroke="var(--red-dark)" stroke-width="8" stroke-dasharray="80 20" stroke-dashoffset="25"/><circle cx="21" cy="21" r="15.915" fill="none" stroke="var(--pink)" stroke-width="8" stroke-dasharray="20 80" stroke-dashoffset="-55"/></svg></div>
    </div>
  </div>

  <div class="pitch">
    <h1 class="headline">Que tal <b>receber novos clientes</b> para almoçar <b>todos os dias</b> no seu restaurante?</h1>
    <div class="preview" role="img" aria-label="Vista em perspectiva do painel do restaurante com gráficos e indicadores"></div>
    <ol class="steps">
      <li><span class="num">1</span><span>O restaurante <b>cadastra</b> seu <b>cardápio</b>, suas <b>informações</b> e <b>imagens</b> no <b>Grupo da Mesada</b>.</span></li>
      <li><span class="num">2</span><span>O <b>Grupo da Mesada</b> leva <b>novos clientes</b> de uma <b>região</b> para o restaurante.</span></li>
      <li><span class="num">3</span><span>Restaurante <b>recebe o valor</b> dos <b>usuários</b>.</span></li>
    </ol>
  </div>
</section>
</body>
</html>
```